Tri Fold Brochure - Harborline Capital Circle

Partnered Asset Builders LLC Harborline Capital Circle
Partnered Asset Builders LLC also has a Harborline Capital Circle, administered by Senior Member Malcolm Fairweather. The Harborline Capital Circle gives select investors access to real estate opportunities across Florida’s desirable coastal counties. Our focus is on county tax deed sales, where properties may be acquired below estimated market value and offer potential for resale, rental income, redevelopment, or long-term growth.
Through market research, property analysis, and acquisition planning, we identify opportunities that are often missed through traditional real estate channels. Using local market insight and a disciplined tax deed strategy, our team targets properties in areas with strong tourism, population growth, economic activity, and steady demand for housing and commercial space.
Partnered Asset Builders offers a collaborative platform where qualified opportunities that have been sourced and reviewed are presented to our Investors for participation. Instead of spending hours searching tax deed sales, investors gain access to these opportunities that have already undergone preliminary review. Profits from successful projects are shared among participating investors according to the terms of each opportunity.
Program Benefits
• Access to real estate opportunities identified through Florida tax deed sales
• Focus on high-demand coastal counties with strong tourism and economic activity
• Professional property sourcing and preliminary due diligence
• Opportunities to acquire properties below estimated market value
• Participation in a collaborative investment model
• Potential income through resale, redevelopment, rental, or appreciation
• Access to opportunities not readily available through traditional real estate markets
Whether you are an experienced investor or looking to diversify your portfolio, the Harborline Capital Circle offers a structured way to participate in Florida real estate opportunities.
Shoreward Holdings is administered by Partnered Asset Builders LLC. All investments involve risk, including possible loss of principal. Returns are not guaranteed, and past performance does not guarantee future results. Prospective investors should conduct their own due diligence and consult legal, tax, and financial advisors before making any investment decision.

Understanding Florida Tax Deed Sales
One of the unique advantages of investing in Florida tax deed properties is that Florida operates differently from most states throughout the United States. In many states, delinquent property taxes are sold as tax lien certificates, meaning investors purchase the debt against a property and earn interest while the property owner retains ownership rights. In Florida, however, once statutory requirements have been met and redemption periods have expired, properties may proceed to a Tax Deed Sale, where the actual real estate itself is auctioned to the highest bidder. This process can create opportunities for investors to acquire ownership of real property rather than simply holding a tax lien. Because many tax deed properties receive limited market exposure and are sold through county-administered auctions, acquisition prices may be significantly below estimated market value. For knowledgeable investors who understand the process and conduct proper due diligence, Florida's tax deed system can present unique opportunities not commonly available through traditional real estate acquisitions or tax lien investing programs found in other states.

What Happens After a Successful Tax Deed Purchase?
Once a property is successfully acquired at a Florida Tax Deed Sale, the process of securing ownership is often more straightforward than many investors expect. Unlike traditional real estate transactions that may involve lengthy negotiations, financing contingencies, inspections, appraisals, and extensive closing requirements, a tax deed purchase generally follows a streamlined county-administered process.
After the winning bid is submitted and the required funds are paid, the county clerk typically issues a Tax Deed conveying ownership rights to the successful bidder. The deed is then recorded in the public land records, establishing the investor's ownership interest in the property. In many cases, the administrative costs associated with recording and obtaining the deed are relatively modest when compared to traditional real estate acquisition expenses.
Following the recording of the Tax Deed, investors generally verify the property's status, including occupancy, municipal code compliance, utility availability, and any matters that may affect future use or marketability. Depending on the investment strategy, the property may then be prepared for resale, renovation, rental, redevelopment, or long-term holding.
For investors seeking the highest level of marketability and title assurance, a quiet title action may be pursued. A quiet title action is a legal process used to resolve potential claims or interests that may cloud title and can make the property more attractive to future buyers and lenders. While not every situation is identical, many investors view this as a routine step in maximizing a property's resale value and financing options.
One of the reasons Florida tax deed investing is attractive to many investors is that, after acquisition, the ownership transfer process is often largely administrative in nature. Rather than navigating months of traditional purchase negotiations and financing approvals, investors may be able to move directly into implementing their chosen investment strategy. With proper due diligence and professional guidance, the post-acquisition process can often be managed efficiently while positioning the property for future profit opportunities.
The procedures, costs, and timelines associated with Florida tax deed properties vary by county and property. Investors should consult qualified legal, title, tax, and real estate professionals before making investment decisions.

Why We Focus on Condominium Opportunities
Because Florida tax deed auctions are conducted online and many targeted properties are located hundreds of miles from our investors and acquisition team, it is often impractical to perform a comprehensive interior inspection prior to bidding. As a result, many tax deed properties throughout Florida are acquired based primarily on available public records, county information, satellite imagery, exterior observations, market data, and community research. To help manage risk in this environment, Shoreward Holdings frequently prioritizes condominium opportunities located within established communities.
Condominiums often present several advantages when compared to single-family homes or vacant land acquisitions. Since the condominium association is typically responsible for maintaining the building exterior, roofs, common areas, landscaping, and many structural components, investors are generally exposed to fewer unknown repair items. In addition, condominium units often require less renovation work, lower capital expenditures, and shorter turnaround times to prepare for resale or rental occupancy. By focusing on properties with potentially lower rehabilitation costs and more predictable maintenance requirements, Shoreward Holdings seeks to preserve profit margins while reducing the likelihood that unexpected repair expenses will significantly impact overall project performance.
While no investment is without risk, our emphasis on condominium communities is intended to create a more efficient acquisition strategy that aligns with the realities of online tax deed investing and helps promote disciplined investment decisions.

A Collaborative Investment Model
Partnered Asset Builders LLC ("PAB") was founded on the principle that successful real estate investing is best achieved through collaboration. Each investment opportunity brings together qualified investors who combine financial resources, experience, and expertise to pursue carefully selected real estate acquisitions. Prior to participating in any venture, prospective investors undergo a thorough vetting process designed to promote responsible participation and help ensure that each investment group is comprised of financially capable and like-minded individuals.
For each investment opportunity, profits are generally distributed among the participating investors in proportion to their respective capital contributions, subject to the terms of the applicable Joint Venture Agreement. This structure provides a transparent and equitable framework that aligns each participant's financial interest with the overall success of the project.
Malcolm Fairweather, acting on behalf of Partnered Asset Builders LLC, serves as the Senior Project Manager for each joint venture. In this role, Mr. Fairweather oversees the acquisition process, project coordination, due diligence, renovation planning, investor communications, contractor coordination, disposition strategy, and overall project management from acquisition through final distribution. As compensation for these management services, Partnered Asset Builders LLC generally receives a project management fee equal to five percent (5%) of the approved renovation budget, as specified in the applicable project agreements.
In addition, Partnered Asset Builders LLC is granted the first opportunity, where permitted by law and agreed to by the joint venture participants, to provide mortgage financing and real estate brokerage services that may be required during the acquisition, refinancing, or disposition of a project. Any such services will be provided through appropriately licensed entities and disclosed in accordance with applicable federal and state laws.
Beyond project management, Partnered Asset Builders LLC provides comprehensive administrative support for each venture, including entity formation and business registration (when applicable), preparation and coordination of legal documentation, maintenance of accounting records and bookkeeping, financial reporting, record retention, and general administrative oversight. This centralized management approach enables investors to focus on the investment opportunity while PAB coordinates the operational and administrative functions necessary to help each project proceed efficiently and professionally.

For more information, contact Malcolm Fairweather directly at (240) 555-0187 or malcolm@pabllc-example.com

```html
<!DOCTYPE html>
<html lang="en">
<head>
<meta charset="utf-8">
<title>Harborline Capital Circle – Tri Fold Brochure</title>
<link rel="stylesheet" href="https://fonts.googleapis.com/css2?family=Montserrat:wght@400;500;600;700&family=Inter:wght@400;600&display=swap">
<style>
  :root{
    --navy:#1c2a55;
    --navy-deep:#16214a;
    --gold:#c9a45c;
    --paper:#f6f6f4;
    --ink:#2b2f3a;
    --backdrop:#e2e3e7;
    --sky-top:#8fb2d6;
    --sky-low:#dbe6ef;
    --sea:#4f9a8a;
  }
  *{box-sizing:border-box;margin:0;padding:0}
  html,body{width:1200px;height:1200px;overflow:hidden}
  body{background:var(--backdrop);font-family:"Inter",Arial,sans-serif;color:var(--ink);position:relative}
  .brochure{position:absolute;left:39px;top:290px;display:flex;gap:14px}
  .panel{position:relative;width:270px;height:620px;background:var(--paper);overflow:hidden;box-shadow:0 6px 18px rgba(20,30,60,.15)}
  .body-text{font-size:7.6px;line-height:1.42}
  .body-text p{margin-bottom:6px}
  .panel-heading{font-family:"Montserrat",sans-serif;font-weight:700;color:var(--navy);font-size:11.5px;letter-spacing:.4px;text-transform:uppercase;line-height:1.25}
  .gold{color:var(--gold)}
  .band{position:absolute;left:0;bottom:0;width:100%}
  .band svg{display:block}

  /* panel 1 */
  .panel--model .upper{position:absolute;left:20px;right:20px;top:22px}
  .panel--model .upper .panel-heading{margin-bottom:8px}
  .panel--model .lower{position:absolute;left:0;top:318px;width:100%;height:302px;background:var(--navy);color:#fff;padding:30px 20px 0}
  .panel--model .lower .panel-heading{color:#fff;margin-bottom:8px}
  .panel--model .lower .body-text{color:#dfe3ee}
  .service-mark{display:flex;gap:8px;align-items:flex-start;margin-top:4px}
  .service-mark .square{width:16px;height:16px;border:1.2px solid var(--gold);flex:none}
  .service-mark span{font-size:7px;color:#dfe3ee;line-height:1.35}
  .contact{position:absolute;left:20px;right:20px;bottom:18px;border-top:1px solid var(--gold);padding-top:8px;font-size:7.6px;color:#fff;line-height:1.5}
  .contact strong{font-family:"Montserrat",sans-serif;font-size:9px;letter-spacing:.6px;color:var(--gold)}

  /* panel 2 */
  .interior-photo{position:absolute;left:0;top:0;width:100%;height:215px;background:linear-gradient(160deg,#cfd8df 0%,#e9e6df 45%,#b9a892 100%)}
  .benefits{position:absolute;left:20px;right:18px;top:240px}
  .benefits .panel-heading{font-size:13px;margin-bottom:10px}
  .benefits ul{list-style:none;font-size:7.8px;line-height:1.4}
  .benefits li{position:relative;padding-left:11px;margin-bottom:6px}
  .benefits li::before{content:"";position:absolute;left:0;top:3px;width:5px;height:5px;background:var(--gold)}
  .benefits .closing{font-size:7.8px;line-height:1.4;margin-top:8px;font-style:italic}
  .panel--benefits .band-text{position:absolute;left:0;right:0;bottom:26px;text-align:center;font-family:"Montserrat",sans-serif;color:#fff;font-size:9.5px;font-weight:600;letter-spacing:.6px;line-height:1.45}
  .panel--benefits .band-text .gold{display:block}

  /* panel 3 */
  .intro{position:absolute;left:22px;right:20px;top:24px;font-size:8.4px;line-height:1.48}
  .intro p{margin-bottom:11px}
  .intro strong{color:var(--navy)}
  .panel--intro .band-text{position:absolute;left:0;right:0;bottom:20px;text-align:center;font-family:"Montserrat",sans-serif;font-size:8.6px;letter-spacing:.4px;color:#fff;font-weight:500;line-height:1.6}
  .panel--intro .band-icon{position:absolute;left:50%;bottom:62px;transform:translateX(-50%)}

  /* panel 4 */
  .cover-head{position:absolute;left:0;right:0;top:26px;text-align:center}
  .brand-name{display:inline-flex;align-items:center;gap:7px;font-family:"Montserrat",sans-serif;font-weight:600;color:var(--navy);font-size:12px;letter-spacing:1.4px}
  .brand-name .square{width:10px;height:10px;background:var(--navy)}
  .cover-title{font-family:"Montserrat",sans-serif;font-weight:600;color:var(--navy);font-size:36px;letter-spacing:.5px;margin-top:30px;line-height:1}
  .cover-sub{font-family:"Montserrat",sans-serif;font-weight:500;color:var(--gold);font-size:17px;letter-spacing:.5px;margin-top:6px}
  .divider{margin:10px auto 0;display:block}
  .skyline-photo{position:absolute;left:0;top:190px;width:100%;height:360px;background:linear-gradient(180deg,var(--paper) 0%,var(--sky-low) 18%,var(--sky-top) 48%,#c8cdd2 70%,var(--sea) 100%)}
  .cover-foot{position:absolute;left:0;right:0;bottom:22px;text-align:center;font-family:"Montserrat",sans-serif;font-size:8.2px;letter-spacing:.4px;color:#fff;line-height:1.6;font-weight:500}
  .cover-foot .rule{width:170px;height:1px;background:var(--gold);margin:0 auto 6px}
  .cover-seal{position:absolute;left:50%;bottom:76px;transform:translateX(-50%)}
</style>
</head>
<body>
<main class="brochure">

  <!-- inside flap: model and contact -->
  <section class="panel panel--model">
    <div class="upper">
      <h2 class="panel-heading">Why We Focus on<br>Condominium Opportunities</h2>
      <div class="body-text">
        <p>Because Florida tax deed auctions are conducted online and many targeted properties are located hundreds of miles from our investors, it is often impractical to perform an interior inspection prior to bidding.</p>
        <p>To help manage risk, Shoreward Holdings frequently prioritizes condominium opportunities located within established communities.</p>
        <p>The association typically maintains exteriors, roofs, and common areas, so condominium units often need less renovation and shorter turnaround times.</p>
        <p>Our emphasis on condominium communities is intended to create a more efficient strategy that aligns with the realities of online tax deed investing.</p>
      </div>
    </div>
    <div class="lower">
      <h2 class="panel-heading">A Collaborative<br>Investment Model</h2>
      <div class="body-text">
        <p>Partnered Asset Builders LLC ("PAB") was founded on the principle that successful real estate investing is best achieved through collaboration.</p>
        <p>Malcolm Fairweather, acting on behalf of PAB, serves as the Senior Project Manager for each joint venture, receiving a fee of five percent (5%) of the approved renovation budget.</p>
      </div>
      <div class="service-mark"><div class="square"></div><span>First Opportunity for Mortgage &amp; Brokerage Services</span></div>
      <div class="contact">
        <strong>CONTACT</strong><br>
        Malcolm Fairweather directly<br>
        (240) 555-0187 · malcolm@pabllc-example.com
      </div>
    </div>
  </section>

  <!-- inside middle: benefits -->
  <section class="panel panel--benefits">
    <div class="interior-photo" role="img" aria-label="Bright coastal condominium interior with dining area and ocean view windows"></div>
    <svg class="wedge" style="position:absolute;left:0;top:150px" width="270" height="80" viewBox="0 0 270 80" aria-hidden="true">
      <polygon points="140,80 270,10 270,80" fill="var(--navy)"/>
      <path d="M0,80 L270,6" stroke="var(--gold)" stroke-width="2" fill="none"/>
      <polygon points="0,80 270,8 270,80" fill="var(--paper)" opacity="0"/>
    </svg>
    <div class="benefits">
      <h2 class="panel-heading">Program Benefits</h2>
      <ul>
        <li>Access to real estate opportunities identified through Florida tax deed sales</li>
        <li>Focus on high-demand coastal counties with strong tourism and economic activity</li>
        <li>Professional property sourcing and preliminary due diligence</li>
        <li>Opportunities to acquire properties below estimated market value</li>
        <li>Participation in a collaborative investment model</li>
        <li>Potential income through resale, redevelopment, rental, or appreciation</li>
        <li>Access to opportunities not readily available through traditional real estate markets</li>
      </ul>
      <p class="closing">Whether you are an experienced investor or looking to diversify your portfolio, the Harborline Capital Circle offers a structured way to participate in Florida real estate opportunities.</p>
    </div>
    <div class="band">
      <svg width="270" height="90" viewBox="0 0 270 90" aria-hidden="true">
        <path d="M0,22 Q135,-8 270,22 L270,90 L0,90 Z" fill="var(--navy)"/>
        <path d="M0,22 Q135,-8 270,22" stroke="var(--gold)" stroke-width="2" fill="none"/>
      </svg>
    </div>
    <div class="band-text">SHOREWARD HOLDINGS<span class="gold">ADMINISTERED BY<br>PARTNERED ASSET BUILDERS LLC.</span></div>
  </section>

  <!-- inside right: introduction -->
  <section class="panel panel--intro">
    <div class="intro">
      <p>Partnered Asset Builders LLC also has a <strong>Harborline Capital Circle</strong>, administered by Senior Member <strong>Malcolm Fairweather</strong>.</p>
      <p>The Harborline Capital Circle gives select investors access to real estate opportunities across Florida’s desirable coastal counties.</p>
      <p>Our focus is on county tax deed sales, where properties may be acquired below estimated market value and offer potential for resale, rental income, redevelopment, or long-term growth.</p>
      <p>Through market research, property analysis, and acquisition planning, we identify opportunities that are often missed through traditional real estate channels. Using local market insight and a disciplined tax deed strategy, our team targets properties in areas with strong tourism, population growth, economic activity, and steady demand for housing and commercial space.</p>
      <p>Partnered Asset Builders offers a collaborative platform where qualified opportunities that have been sourced and reviewed are presented to our Investors for participation. Instead of spending hours searching tax deed sales, investors gain access to these opportunities that have already undergone preliminary review. Profits from successful projects are shared among participating investors according to the terms of each opportunity.</p>
    </div>
    <div class="band">
      <svg width="270" height="130" viewBox="0 0 270 130" aria-hidden="true">
        <path d="M0,40 Q70,40 135,10 Q200,-12 270,22 L270,130 L0,130 Z" fill="var(--navy)"/>
        <path d="M0,40 Q70,40 135,10 Q200,-12 270,22" stroke="var(--gold)" stroke-width="2" fill="none"/>
      </svg>
    </div>
    <svg class="band-icon" width="46" height="30" viewBox="0 0 46 30" aria-hidden="true">
      <g fill="var(--gold)">
        <circle cx="10" cy="9" r="4.5"/><rect x="3" y="15" width="14" height="14" rx="3"/>
        <circle cx="36" cy="9" r="4.5"/><rect x="29" y="15" width="14" height="14" rx="3"/>
        <circle cx="23" cy="6" r="5.5"/><rect x="15" y="13" width="16" height="17" rx="3"/>
      </g>
    </svg>
    <div class="band-text">COLLABORATIVE INVESTING.<br><span class="gold">SHARED SUCCESS.</span></div>
  </section>

  <!-- cover -->
  <section class="panel panel--cover">
    <div class="skyline-photo" role="img" aria-label="Aerial view of coastal high-rise towers along a beach under a blue sky"></div>
    <div class="cover-head">
      <div class="brand-name"><span class="square"></span>PARTNERED ASSET BUILDERS LLC</div>
      <h1 class="cover-title">HARBORLINE</h1>
      <div class="cover-sub">CAPITAL CIRCLE</div>
      <svg class="divider" width="160" height="10" viewBox="0 0 160 10" aria-hidden="true">
        <line x1="0" y1="5" x2="72" y2="5" stroke="var(--gold)" stroke-width="1"/>
        <rect x="77" y="2" width="6" height="6" transform="rotate(45 80 5)" fill="var(--gold)"/>
        <line x1="88" y1="5" x2="160" y2="5" stroke="var(--gold)" stroke-width="1"/>
      </svg>
    </div>
    <div class="band">
      <svg width="270" height="150" viewBox="0 0 270 150" aria-hidden="true">
        <path d="M0,50 Q135,-10 270,40 L270,150 L0,150 Z" fill="var(--navy-deep)"/>
        <path d="M0,50 Q135,-10 270,40" stroke="var(--gold)" stroke-width="2.2" fill="none"/>
      </svg>
    </div>
    <svg class="cover-seal" width="40" height="40" viewBox="0 0 40 40" aria-hidden="true">
      <circle cx="20" cy="20" r="18" fill="none" stroke="var(--gold)" stroke-width="1.6"/>
    </svg>
    <div class="cover-foot">
      <div class="rule"></div>
      INVESTING IN FLORIDA’S COAST.<br><span class="gold">BUILDING YOUR FUTURE.</span>
    </div>
  </section>

</main>
</body>
</html>
```